Business Card Design

Melodex Podcast

Industry/Entity Type

Business

Contact Information for Business Card

YOU ARE INVITED TO LISTEN
Stretch Every Idea
Award Winning Melodex Podcast
with Dr. Marla Quenby
www.drmarlaquenby-example.com

555-018-7364

```html
<!DOCTYPE html>
<html lang="en">
<head>
<meta charset="utf-8">
<title>Stretch Every Idea – Business Card</title>
<link href="https://fonts.googleapis.com/css2?family=Ubuntu:ital,wght@0,400;0,700;1,700&display=swap" rel="stylesheet">
<style>
  :root {
    --ink: #121212;
    --paper: #ffffff;
    --ribbon: #f1f1f1;
    --lime: #86cf2a;
    --lime-soft: #d6f0a6;
    --steel: #b4b9bf;
    --steel-dark: #8d9399;
  }
  html, body {
    margin: 0;
    padding: 0;
    width: 1200px;
    height: 702px;
    overflow: hidden;
    background: var(--paper);
  }
  .card {
    position: relative;
    width: 1200px;
    height: 702px;
    background: var(--paper);
    font-family: "Ubuntu", sans-serif;
    color: var(--ink);
    overflow: hidden;
  }
  .mic-photo {
    position: absolute;
    top: 0;
    left: 740px;
    width: 460px;
    height: 702px;
    background:
      linear-gradient(180deg, rgba(180,185,191,0) 8%, rgba(180,185,191,0.85) 22%, var(--steel) 55%, var(--steel-dark) 80%, rgba(141,147,153,0.6) 100%) 90px 0 / 340px 100% no-repeat,
      linear-gradient(90deg, var(--paper) 0%, var(--lime-soft) 22%, var(--lime) 100%);
  }
  .ribbon-art {
    position: absolute;
    left: 22px;
    top: 12px;
    width: 648px;
    height: 276px;
    background: var(--ribbon);
  }
  .ribbon-text {
    position: absolute;
    left: 58px;
    top: 136px;
    width: 580px;
    margin: 0;
    font-size: 40px;
    line-height: 44px;
    white-space: nowrap;
    text-align: center;
    transform: rotate(-6deg);
    transform-origin: center;
  }
  .ribbon-text .you { font-weight: 700; font-style: italic; }
  .ribbon-text .listen { font-weight: 700; }
  .intro {
    position: absolute;
    left: 38px;
    top: 272px;
    margin: 0;
    font-size: 40px;
    line-height: 55px;
    font-weight: 400;
  }
  .intro .line { display: block; white-space: nowrap; }
  .intro strong { font-weight: 700; }
  .contact {
    position: absolute;
    left: 135px;
    margin: 0;
    white-space: nowrap;
  }
  .contact-phone { top: 522px; font-size: 58px; line-height: 58px; }
  .contact-web { top: 618px; font-size: 42px; line-height: 46px; }
  .icon {
    position: absolute;
    fill: none;
    stroke: var(--ink);
  }
</style>
</head>
<body>
<main class="card">
  <div class="mic-photo" role="img" aria-label="Photograph of a chrome vintage studio microphone on a lime green background"></div>

  <div class="ribbon-art" role="img" aria-label="Decorative scroll ribbon banner"></div>
  <p class="ribbon-text"><span class="you">YOU</span> ARE INVITED TO <span class="listen">LISTEN</span></p>

  <p class="intro">
    <strong class="line">Stretch Every Idea</strong>
    <span class="line">Award Winning Melodex</span>
    <span class="line">Podcast with <strong>Dr. Marla</strong></span>
    <strong class="line">Quenby</strong>
  </p>

  <svg class="icon icon-phone" style="left:48px;top:508px" width="48" height="90" viewBox="0 0 48 90" aria-hidden="true">
    <rect x="3" y="3" width="42" height="84" rx="7" stroke-width="5" fill="var(--paper)"/>
    <rect x="3" y="3" width="42" height="11" rx="6" fill="var(--ink)" stroke="none"/>
    <rect x="3" y="74" width="42" height="13" rx="6" fill="var(--ink)" stroke="none"/>
  </svg>
  <p class="contact contact-phone">555-018-7364</p>

  <svg class="icon icon-web" style="left:28px;top:610px" width="88" height="66" viewBox="0 0 88 66" aria-hidden="true">
    <rect x="3" y="3" width="82" height="48" stroke-width="4.5" fill="var(--paper)"/>
    <path d="M38,51 L38,60 M50,51 L50,60" stroke-width="5"/>
    <rect x="28" y="58" width="32" height="6" fill="var(--ink)" stroke="none"/>
  </svg>
  <p class="contact contact-web">www.drmarlaquenby-example.com</p>
</main>
</body>
</html>
```